Business Card - Tally Forge

Need Business Card design for company named Tally Forge. Software development focused mainly on Brindle Kelvox & Vuro Apps. I've attached our logo with both a black and white background. Please add trademark symbol to logo when using.

```html
<!DOCTYPE html>
<html lang="en">
<head>
<meta charset="utf-8">
<title>Tally Forge Business Card</title>
<link href="https://fonts.googleapis.com/css2?family=Open+Sans:wght@400;600;700&display=swap" rel="stylesheet">
<style>
  :root {
    --backdrop: #7a5e3e;
    --card-white: #ffffff;
    --brand-yellow: #f7c21a;
    --brand-red: #db1f2a;
    --brand-black: #0d0d0d;
    --ink: #1a1a1a;
    --label-yellow: #fbc02d;
  }
  html, body {
    margin: 0;
    padding: 0;
    width: 1200px;
    height: 1014px;
    overflow: hidden;
    background: var(--backdrop);
    font-family: "Open Sans", sans-serif;
  }
  .stage {
    position: relative;
    width: 1200px;
    height: 1014px;
  }
  .card {
    position: absolute;
    width: 340px;
    height: 595px;
    top: 210px;
    overflow: hidden;
    box-shadow: 0 14px 30px rgba(0,0,0,0.35);
  }
  .card-front {
    left: 190px;
    background: var(--card-white);
  }
  .card-back {
    left: 670px;
    background: linear-gradient(100deg, #050505 0%, #2a2a2a 55%, #0a0a0a 100%);
  }
  .front-header {
    height: 295px;
    display: flex;
    align-items: center;
    justify-content: center;
  }
  .brand-name {
    font-weight: 700;
    font-size: 34px;
    color: var(--ink);
    letter-spacing: -0.5px;
    display: flex;
    align-items: center;
    gap: 10px;
  }
  .brand-dot {
    width: 14px;
    height: 14px;
    border-radius: 50%;
    background: var(--brand-yellow);
  }
  .name-band {
    height: 96px;
    background: linear-gradient(90deg, var(--brand-yellow), #fbd34a 45%, var(--brand-yellow));
    border-bottom: 5px solid var(--card-white);
    display: flex;
    flex-direction: column;
    align-items: center;
    justify-content: center;
  }
  .person-name {
    font-weight: 700;
    font-size: 26px;
    color: var(--ink);
    line-height: 1.1;
  }
  .person-role {
    font-size: 22px;
    color: var(--brand-red);
    line-height: 1.2;
  }
  .contact-block {
    height: 199px;
    background: var(--brand-red);
    color: var(--card-white);
    padding: 22px 0 0 40px;
    box-sizing: border-box;
    font-size: 17px;
    line-height: 1.45;
  }
  .contact-line { margin: 0; }
  .contact-label { color: var(--label-yellow); }
  .address { margin-top: 8px; }
  .back-mark {
    position: absolute;
    right: 0;
    top: 150px;
    width: 170px;
    height: 300px;
    background: var(--brand-yellow);
    border-radius: 40px 0 0 40px;
    display: flex;
    flex-direction: column;
    align-items: center;
    justify-content: center;
    gap: 14px;
  }
  .back-mark .brand-name {
    color: var(--card-white);
    font-size: 26px;
    writing-mode: vertical-rl;
  }
  .back-dot {
    width: 36px;
    height: 36px;
    border-radius: 50%;
    background: var(--card-white);
  }
  .web-address {
    position: absolute;
    left: 34px;
    top: 410px;
    color: var(--brand-red);
    font-weight: 600;
    font-size: 18px;
  }
</style>
</head>
<body>
<main class="stage">
  <section class="card card-front" aria-label="Card front">
    <header class="front-header">
      <div class="brand-name"><span class="brand-dot"></span>Tally Forge</div>
    </header>
    <div class="name-band">
      <div class="person-name">Dean Marsh</div>
      <div class="person-role">Manager</div>
    </div>
    <div class="contact-block">
      <p class="contact-line">555-214-3870 <span class="contact-label">Mobile</span></p>
      <p class="contact-line">555-309-6142 <span class="contact-label">Office</span></p>
      <p class="contact-line">555-471-9026 <span class="contact-label">Fax</span></p>
      <p class="contact-line">dean.marsh@tallyforge.com</p>
      <p class="contact-line address">4120 Harbor Rd</p>
      <p class="contact-line">Oakvale, FL 33990</p>
    </div>
  </section>
  <section class="card card-back" aria-label="Card back">
    <div class="back-mark">
      <span class="back-dot"></span>
      <div class="brand-name">Tally Forge</div>
    </div>
    <div class="web-address">tallyforge.com</div>
  </section>
</main>
</body>
</html>
```